Redesign of iOS App Lumo Tutor

Redesign of existing App Lumo Tutor, an app that helps learning Japanese Kanjis, Hiragana, Katakana.

The functionallity should remain the same as today: the app is free, you may download it at the app store. But: I like the design of my other apps better ;)

Target Market(s)

Students learning Japanese

Industry/Entity Type

Teacher

Font styles to use
Sans Serif

Requirements
Must have
• Lumo Tutor has 7 main screens, all screens has to be designed for iPhone and iPad: Main, Settings, Reading Tests, Writing Tests, Game, Paper Mode, Search
Nice to have
• I like the logo as it is today

```html
<!DOCTYPE html>
<html lang="en">
<head>
<meta charset="utf-8">
<title>Lumo Tutor – Reading Test</title>
<link rel="stylesheet" href="https://fonts.googleapis.com/css2?family=Montserrat:wght@400;500;700&family=Noto+Sans+JP:wght@400;500&display=swap">
<style>
  :root{
    --page:#eceef1;
    --screen:#ffffff;
    --ink:#1b1b1b;
    --muted:#8a8d94;
    --line:#b9bcc2;
    --wrong:#dd2611;
    --correct:#6cc2af;
    --button:#efefef;
  }
  *{box-sizing:border-box;margin:0;padding:0}
  html,body{width:1200px;height:1200px;overflow:hidden;background:var(--page)}
  body{font-family:"Montserrat",sans-serif;color:var(--ink);position:relative}

  .screen{
    position:absolute;left:300px;top:67px;width:600px;height:1066px;
    background:var(--screen);border-radius:8px;overflow:hidden;
    box-shadow:0 10px 40px rgba(0,0,0,.12);
  }

  .status-bar{
    height:34px;display:flex;align-items:center;justify-content:space-between;
    padding:0 14px;font-size:17px;color:var(--muted);
  }
  .status-bar .carrier{display:flex;align-items:center;gap:6px}
  .status-bar .dots{display:flex;gap:3px}
  .status-bar .dots i{width:8px;height:8px;border-radius:50%;background:var(--muted);display:block}
  .status-bar .battery{display:flex;align-items:center;gap:6px}
  .battery-icon{width:38px;height:16px;border:1.5px solid var(--muted);border-radius:3px;padding:2px;position:relative}
  .battery-icon::before{content:"";display:block;height:100%;background:var(--muted);border-radius:1px}
  .battery-icon::after{content:"";position:absolute;right:-5px;top:4px;width:3px;height:6px;background:var(--muted);border-radius:0 2px 2px 0}

  .score-bar{
    height:100px;display:flex;justify-content:space-around;align-items:center;
    padding:0 30px;border-bottom:1.5px solid var(--line);
    box-shadow:0 2px 4px rgba(0,0,0,.08);
  }
  .score{display:flex;align-items:baseline;gap:8px;font-size:17px}
  .score b{font-weight:500;font-size:26px}
  .score.remaining{color:var(--ink)}
  .score.wrong{color:var(--wrong)}
  .score.correct{color:var(--correct)}

  .prompt{text-align:center;padding-top:24px;height:200px}
  .prompt .kanji{font-family:"Noto Sans JP",sans-serif;font-size:84px;line-height:1.1;font-weight:400}
  .prompt .readings{font-family:"Noto Sans JP",sans-serif;font-size:21px;color:var(--muted);letter-spacing:2px;margin-top:8px}

  .answer-grid{
    display:grid;grid-template-columns:repeat(3,160px);grid-auto-rows:160px;gap:16px;
    justify-content:center;
  }
  .tile{
    border:1.5px solid var(--line);border-radius:4px;display:flex;align-items:center;justify-content:center;
    font-size:27px;font-weight:400;background:var(--screen);
  }
  .tile.is-wrong{background:var(--wrong);border-color:var(--wrong);color:#fff;box-shadow:3px 4px 0 #2a2a2a}
  .tile.is-correct{background:var(--correct);border-color:var(--correct);color:#fff;box-shadow:3px 4px 0 #2a2a2a}

  .action-bar{
    position:absolute;left:0;right:0;bottom:60px;height:120px;
    display:flex;align-items:center;justify-content:center;
  }
  .action-bar .pill{
    width:210px;height:70px;background:var(--button);display:flex;align-items:center;justify-content:center;
    font-weight:700;font-size:22px;letter-spacing:8px;color:#333;
  }
  .action-bar .home{border-radius:10px 0 0 10px;margin-right:-14px}
  .action-bar .skip{border-radius:0 10px 10px 0;margin-left:-14px}
  .action-bar .current{
    width:120px;height:120px;border-radius:50%;background:var(--button);border:8px solid #fff;
    display:flex;align-items:center;justify-content:center;position:relative;z-index:1;
    font-family:"Noto Sans JP",sans-serif;font-size:52px;
  }
</style>
</head>
<body>
  <main class="screen">
    <header class="status-bar">
      <div class="carrier">
        <span class="dots"><i></i><i></i><i></i><i></i><i></i></span>
        <span>Nimbus</span>
        <svg width="20" height="15" viewBox="0 0 20 15" aria-hidden="true"><path d="M10 14 L7 10.5 A4.5 4.5 0 0 1 13 10.5Z M3.8 7.5 A9 9 0 0 1 16.2 7.5 L14.6 9.2 A6.6 6.6 0 0 0 5.4 9.2Z M0.7 4.3 A13.5 13.5 0 0 1 19.3 4.3 L17.7 6 A11 11 0 0 0 2.3 6Z" fill="#8a8d94"/></svg>
      </div>
      <span class="time">11:55 AM</span>
      <div class="battery"><span>100%</span><span class="battery-icon"></span></div>
    </header>

    <section class="score-bar">
      <div class="score remaining">Remaining <b>171</b></div>
      <div class="score wrong">Wrong <b>13</b></div>
      <div class="score correct">Correct <b>6</b></div>
    </section>

    <section class="prompt">
      <div class="kanji">名</div>
      <div class="readings">メイ, ミョウ, な</div>
    </section>

    <section class="answer-grid">
      <div class="tile">seven</div>
      <div class="tile is-wrong">person</div>
      <div class="tile">long</div>
      <div class="tile is-correct">name</div>
      <div class="tile">come</div>
      <div class="tile">many</div>
      <div class="tile">write</div>
      <div class="tile">in</div>
      <div class="tile">station</div>
    </section>

    <nav class="action-bar">
      <div class="pill home">HOME</div>
      <div class="current">名</div>
      <div class="pill skip">SKIP</div>
    </nav>
  </main>
</body>
</html>
```